Tutoring Website Needs a Facelift

BrightStudyDesk.com needs a facelift! We are looking to completely redo our website, and logo to give it a more professional, cleaner, and younger vibe.
Our site feels out dated and not very Web 2.0
We are looking to keep the same content on the page now but completely rebrand it to give it the new look we desire.
Updates
Target Market(s)
College Students but needs to portray professionalism, and trust to them
Industry/Entity Type
Tutoring
Look and feel
Each slider illustrates characteristics of the customer's brand and the style your logo design should communicate.

```html
<!DOCTYPE html>
<html lang="en">
<head>
<meta charset="utf-8">
<title>BrightStudyDesk.com</title>
<link href="https://fonts.googleapis.com/css2?family=Montserrat:wght@300;400;500&display=swap" rel="stylesheet">
<style>
:root{
  --page:#f3f3f3;
  --white:#ffffff;
  --ink:#3a3a3a;
  --ink-soft:#555555;
  --blue:#4a90b8;
  --blue-panel:rgba(36,114,160,0.88);
  --blue-deep:#1d4a63;
  --tile:#383838;
  --rule:#e2e2e2;
  --gold:#e0a92a;
  --gold-deep:#b9801a;
  --dot:#4d4f52;
}
*{box-sizing:border-box;margin:0;padding:0}
html,body{width:1108px;height:1200px;overflow:hidden}
body{background:var(--page);font-family:"Montserrat",Arial,sans-serif;color:var(--ink);position:relative}
.abs{position:absolute}

.site-header{left:0;top:0;width:1108px;height:106px;background:var(--page)}
.brand{left:120px;top:44px;font-size:26px;font-weight:400;color:var(--blue);letter-spacing:-0.3px}
.main-nav{left:433px;top:54px;display:flex;font-size:15px;color:var(--ink);font-weight:400}
.main-nav span.sep{margin:0 21px;color:var(--ink)}

.hero{left:0;top:106px;width:1108px;height:413px}
.hero-photo{position:absolute;inset:0;background:
  radial-gradient(ellipse at 78% 40%,#d9b79c 0,#c79f86 18%,transparent 40%),
  radial-gradient(ellipse at 55% 75%,#e7c7a4 0,transparent 35%),
  linear-gradient(90deg,#ffffff 0%,#f4f1ea 15%,#c9b89a 45%,#a7b780 70%,#8fc06a 85%,#cfd4c4 100%)}
.hero-card{position:absolute;left:120px;top:107px;width:425px;height:189px;background:var(--blue-panel);padding:24px 20px}
.hero-card h1{font-size:22px;font-weight:400;color:var(--white);line-height:33px}
.hero-btn{position:absolute;left:19px;top:131px;width:134px;height:37px;background:var(--blue-deep);color:var(--white);font-size:16px;text-align:center;line-height:37px}
.slider-dots{position:absolute;left:117px;top:349px;display:flex;gap:3px}
.slider-dots i{display:block;width:17px;height:17px;border-radius:50%;background:var(--dot)}
.slider-dots i.on{background:#1f4f6b}

.works-band{left:0;top:519px;width:1108px;height:56px;border-top:1px solid var(--rule);border-bottom:1px solid var(--rule);text-align:center;font-size:21px;color:var(--blue);line-height:62px;font-weight:400}

.step{top:591px;width:129px}
.step-tile{height:125px;background:var(--tile);border-radius:3px;position:relative}
.step-tile b{position:absolute;left:12px;top:12px;color:var(--white);font-size:16px;font-weight:400}
.step-tile svg{position:absolute;left:40px;top:52px}
.step p{margin-top:15px;font-size:11px;line-height:16.5px;text-align:center;color:var(--ink-soft);padding:0 2px}

.section-rule{left:0;top:833px;width:1108px;height:1px;background:var(--rule)}
.col-title{font-size:16px;font-weight:400;color:var(--ink)}
.badge{left:132px;top:898px}
.promise{left:282px;width:380px;font-size:11px;line-height:19.5px;color:var(--ink-soft)}
.promise svg{position:absolute;left:0;top:1px}
.promise p{margin-left:25px}
.col-divider{left:677px;top:854px;width:1px;height:213px;background:#dcdcdc}
.news-text{left:710px;top:917px;width:280px;font-size:11px;line-height:22px;color:var(--ink-soft)}
.email{left:711px;top:993px;width:277px;height:34px;background:var(--white);border:1px solid #e6e6e6;font-size:11px;color:#9a9a9a;padding:10px 10px}
.signup{left:711px;top:1035px;width:81px;height:34px;background:linear-gradient(#5b5b5b,#2f2f2f);border-radius:2px;color:var(--white);font-size:11px;text-align:center;line-height:34px}

.footer-rule{left:0;top:1100px;width:1108px;height:1px;background:var(--rule)}
.foot-nav{left:122px;top:1121px;display:flex;font-size:13px;color:var(--ink)}
.foot-nav span.sep{margin:0 18px}
.copyright{left:122px;top:1152px;font-size:11px;color:var(--ink-soft)}
.social{left:877px;top:1123px;display:flex;gap:4px}
.social i{display:block;width:34px;height:34px;border-radius:50%;background:#2e2e2e}
</style>
</head>
<body>

<header class="site-header abs">
  <div class="brand abs">BrightStudyDesk.com</div>
  <nav class="main-nav abs">
    <span>Home</span><span class="sep">|</span>
    <span>Submission Form</span><span class="sep">|</span>
    <span>Testimonials</span><span class="sep">|</span>
    <span>FAQ</span><span class="sep">|</span>
    <span>Contact Us</span>
  </nav>
</header>

<section class="hero abs">
  <div class="hero-photo" role="img" aria-label="Photo of smiling college students outdoors in front of a campus building"></div>
  <div class="hero-card">
    <h1>BrightStudyDesk.com<br>was designed by College Students<br>for College Students</h1>
    <div class="hero-btn">Read More</div>
  </div>
  <div class="slider-dots"><i class="on"></i><i></i><i></i><i></i></div>
</section>

<div class="works-band abs">HOW IT WORKS</div>

<div class="step abs" style="left:120px">
  <div class="step-tile"><b>Step 1</b>
    <svg width="50" height="56" viewBox="0 0 50 56"><path d="M8 2h26l10 10v42H8z" fill="#fff"/><path d="M34 2v10h10" fill="#ccc"/><g stroke="#383838" stroke-width="2"><line x1="14" y1="20" x2="38" y2="20"/><line x1="14" y1="27" x2="38" y2="27"/><line x1="14" y1="34" x2="38" y2="34"/><line x1="14" y1="41" x2="38" y2="41"/><line x1="14" y1="48" x2="38" y2="48"/></g></svg>
  </div>
  <p>Complete For<br>Submission</p>
</div>

<div class="step abs" style="left:268px">
  <div class="step-tile"><b>Step 2</b>
    <svg width="50" height="50" viewBox="0 0 50 50"><g fill="#fff"><rect x="20" y="-4" width="10" height="54" transform="rotate(45 25 25)"/><rect x="20" y="-2" width="10" height="50" transform="rotate(-45 25 25)"/></g><g stroke="#383838" stroke-width="1.5"><line x1="14" y1="10" x2="18" y2="14"/><line x1="22" y1="18" x2="26" y2="22"/></g></svg>
  </div>
  <p>Assigment is<br>Reviewed</p>
</div>

<div class="step abs" style="left:415px">
  <div class="step-tile"><b>Step 3</b>
    <svg width="54" height="56" viewBox="0 0 54 56"><circle cx="27" cy="31" r="22" fill="none" stroke="#fff" stroke-width="3"/><rect x="23" y="3" width="8" height="5" fill="#fff"/><polyline points="27,18 27,32 36,32" fill="none" stroke="#fff" stroke-width="3"/></svg>
  </div>
  <p>You will receive a confirmation email verifying the assignment, duedate and price within 30 minutes</p>
</div>

<div class="step abs" style="left:564px">
  <div class="step-tile"><b>Step 4</b>
    <svg width="62" height="50" viewBox="0 0 62 50"><g fill="#fff"><rect x="22" y="4" width="38" height="5"/><rect x="22" y="12" width="38" height="5"/><rect x="22" y="20" width="38" height="5"/><rect x="22" y="28" width="38" height="5"/><rect x="22" y="36" width="38" height="5"/><rect x="22" y="44" width="38" height="5"/><circle cx="16" cy="32" r="16"/></g><text x="16" y="39" text-anchor="middle" font-family="Montserrat,Arial,sans-serif" font-size="20" font-weight="500" fill="#383838">$</text></svg>
  </div>
  <p>Payment is due within 24 hours. Your work will not be started until payment is received</p>
</div>

<div class="step abs" style="left:711px">
  <div class="step-tile"><b>Step 5</b>
    <svg width="62" height="48" viewBox="0 0 62 48"><g fill="#fff"><rect x="2" y="16" width="6" height="14"/><path d="M10 14h8l34-12v44L18 34h-8z"/><rect x="54" y="0" width="5" height="46"/><rect x="16" y="34" width="8" height="10"/></g></svg>
  </div>
  <p>You Party</p>
</div>

<div class="step abs" style="left:860px">
  <div class="step-tile"><b>Step 6</b>
    <svg width="56" height="42" viewBox="0 0 56 42"><rect x="1" y="1" width="54" height="40" fill="#fff"/><polyline points="2,2 28,24 54,2" fill="none" stroke="#383838" stroke-width="2"/><line x1="2" y1="40" x2="21" y2="19" stroke="#383838" stroke-width="2"/><line x1="54" y1="40" x2="35" y2="19" stroke="#383838" stroke-width="2"/></svg>
  </div>
  <p>Completed<br>Assignment is sent<br>to your email</p>
</div>

<div class="section-rule abs"></div>

<h2 class="col-title abs" style="left:121px;top:852px">Our guaranteed</h2>
<svg class="badge abs" width="126" height="126" viewBox="0 0 126 126" role="img" aria-label="Guarantee seal">
  <circle cx="63" cy="63" r="62" fill="var(--gold)"/>
  <circle cx="63" cy="63" r="46" fill="#2a2a2a"/>
  <circle cx="63" cy="63" r="24" fill="var(--gold-deep)"/>
</svg>

<div class="promise abs" style="top:918px">
  <svg width="16" height="16" viewBox="0 0 16 16"><circle cx="8" cy="8" r="8" fill="var(--blue)"/><polyline points="6,4 10,8 6,12" fill="none" stroke="#fff" stroke-width="2"/></svg>
  <p>All assignments are originally created for you. We will never share your work with another student nor plagiarize any source.</p>
</div>
<div class="promise abs" style="top:972px">
  <svg width="16" height="16" viewBox="0 0 16 16"><circle cx="8" cy="8" r="8" fill="var(--blue)"/><polyline points="6,4 10,8 6,12" fill="none" stroke="#fff" stroke-width="2"/></svg>
  <p>Privacy. After submission your work takes on its own identity and your name is never associated with it.</p>
</div>

<div class="col-divider abs"></div>

<h2 class="col-title abs" style="left:718px;top:852px">Subscribe to this newsletter</h2>
<p class="news-text abs">Nulla ornare ipsum ut tellus tincidunt vulputate ac purus libero, quis varius ante. Quisque at ar cu massa, ac imperdiet nunc.</p>
<div class="email abs">Enter E-Mail Address</div>
<div class="signup abs">SIGN UP</div>

<div class="footer-rule abs"></div>
<nav class="foot-nav abs">
  <span>Home</span><span class="sep">|</span>
  <span>Submission Form</span><span class="sep">|</span>
  <span>Testimonials</span><span class="sep">|</span>
  <span>FAQ</span><span class="sep">|</span>
  <span>Contact Us</span>
</nav>
<div class="copyright abs">Copyright ©2013 &nbsp;Company Name &nbsp;&nbsp;- All rights reserved</div>
<div class="social abs" aria-label="Social links"><i></i><i></i><i></i></div>

</body>
</html>
```